Mesa VerdaLighting and Design Web Page

We are a Sales Agency that represents 40+ LED Lighting manufacturers primarily in new commercial, industrial and architectural construction projects. We also are active in the Re-Light and Retrofit Lighting market.
Our current web page can be found at www.mesaverdalighting.example. Our local competitors are www.beaconlumenpw.example,. We would like a more dynamic website that will list our manufacturers we represent and links to their websites. Please offer suggestions to provide a more dynamic website using our new logo which is attached. Please use the color scheme from logo. The final design should communicate innovation and expertise in LED lighting.

Target Market(s)

Architects, Lighting designers, Electrical Engineers, Electrical Contractors, Electrical Distributors, Facility Engineers, Energy Engineers

Industry/Entity Type

Construction

Number of Pages Required

5+ page

Font styles to use
Other font styles liked:
• MS Reference Sans Serif, or close to our LOGO font.

Colors
f78f20
959595

Requirements
Must have
• Logo incorporated with matching background, clean professional look based on logo, links to our manufacturers web page
Nice to have
• LED Lighting project stock photos as examples
Should not have
• crowded pages with text

```html
<!DOCTYPE html>
<html lang="en">
<head>
<meta charset="utf-8">
<title>Mesa Verda Lighting &amp; Design</title>
<link href="https://fonts.googleapis.com/css2?family=Montserrat:wght@400;500;600;700&family=Open+Sans:ital,wght@0,400;0,600;1,400&display=swap" rel="stylesheet">
<style>
:root{
  --orange:#e8620f;
  --orange-light:#f78f20;
  --dark:#1c1a19;
  --footer:#2a2827;
  --footer-deep:#201e1d;
  --grey:#959595;
  --text:#555;
  --heading:#222;
  --white:#fff;
  --card:#f1f1f1;
}
*{margin:0;padding:0;box-sizing:border-box}
html,body{width:1200px;height:3015px;overflow:hidden;background:var(--white)}
body{font-family:'Open Sans',Arial,sans-serif;color:var(--text);position:relative}

/* header */
.top{height:126px;position:relative}
.social{position:absolute;left:180px;top:50px;display:flex;gap:10px}
.social span{width:28px;height:28px;border-radius:50%;background:#555;display:block}
.brand{position:absolute;left:0;right:0;top:40px;display:flex;justify-content:center;align-items:center;gap:10px}
.brand i{width:34px;height:34px;border-radius:50%;background:var(--orange);display:block}
.brand b{font-family:'Montserrat',sans-serif;font-weight:700;font-size:22px;color:var(--orange);line-height:1.05;letter-spacing:.5px}
.phone{position:absolute;right:180px;top:46px;font-family:'Montserrat',sans-serif;font-size:24px;color:#333;display:flex;align-items:center;gap:10px}
.phone svg{width:18px;height:18px}

/* nav */
.nav{height:52px;background:var(--dark);display:flex;justify-content:center;align-items:center}
.nav a{font-family:'Montserrat',sans-serif;font-size:12px;font-weight:600;color:var(--white);text-decoration:none;padding:0 25px;text-transform:uppercase}
.nav a.active{color:var(--orange-light)}

/* hero */
.hero{height:512px;position:relative;background:linear-gradient(180deg,#3b5877 0%,#213850 45%,#142333 75%,#0d1822 100%);text-align:center;color:var(--white)}
.hero h1{font-family:'Montserrat',sans-serif;font-weight:700;font-size:40px;line-height:46px;padding-top:126px;text-shadow:0 2px 6px rgba(0,0,0,.5)}
.hero p{font-style:italic;font-size:26px;margin-top:10px}
.btn{display:inline-block;font-family:'Montserrat',sans-serif;font-weight:600;font-size:13px;text-transform:uppercase;color:var(--white);background:var(--orange);border-radius:22px;text-decoration:none}
.hero .btn{margin-top:64px;width:234px;line-height:42px}
.arrow{position:absolute;width:36px;height:36px;border-radius:50%;display:flex;align-items:center;justify-content:center}
.hero .arrow.l{left:24px;top:216px;background:rgba(0,0,0,.55)}
.hero .arrow.r{right:24px;top:216px;background:var(--orange)}
.dots{position:absolute;right:42px;top:258px;width:5px;height:5px;border-radius:50%;background:#fff}

/* services */
.services{height:320px;display:flex;justify-content:center;gap:28px;padding-left:10px}
.service{width:260px;text-align:center}
.drop{width:84px;height:100px;display:block;margin:0 auto}
.service h3{font-family:'Montserrat',sans-serif;font-size:15px;font-weight:600;color:var(--orange);margin-top:18px}
.service p{font-size:11.5px;line-height:17px;margin:8px 10px 0;color:#666}

/* welcome */
.welcome{height:330px;display:flex}
.welcome .photo{width:585px;background:linear-gradient(100deg,#2e3a57 0%,#5b5a62 40%,#c9b9a3 70%,#efe6d9 100%)}
.welcome .copy{flex:1;background:var(--orange);color:var(--white);padding:28px 60px 0 38px}
.welcome h2{font-family:'Montserrat',sans-serif;font-size:28px;font-weight:700}
.welcome p{font-size:12px;line-height:19px;margin-top:12px}
.outline{display:inline-block;margin-top:26px;width:204px;line-height:38px;border:2px solid var(--white);border-radius:22px;text-align:center;font-family:'Montserrat',sans-serif;font-size:12px;font-weight:600;color:var(--white)}

/* section titles */
.title{font-family:'Montserrat',sans-serif;font-size:32px;font-weight:500;color:var(--heading);text-align:center}
.sub{font-size:14px;line-height:21px;text-align:center;color:#777;width:540px;margin:10px auto 0}

/* manufacturers */
.makers{height:488px;position:relative;padding-top:64px}
.maker-row{position:absolute;top:190px;left:155px;display:flex;gap:14px}
.maker{width:213px;height:133px;border:1px solid #e3e3e3;display:flex;flex-direction:column}
.maker .name{flex:1;display:flex;align-items:center;justify-content:center;font-family:'Montserrat',sans-serif;font-size:22px;font-weight:600;color:#333}
.maker .url{height:32px;background:var(--orange);color:var(--white);font-size:12px;font-weight:600;display:flex;align-items:center;justify-content:center}
.ring{position:absolute;width:36px;height:36px;border:1px solid #bbb;border-radius:50%;display:flex;align-items:center;justify-content:center;background:#fff}
.makers .ring.l{left:64px;top:246px}
.makers .ring.r{right:64px;top:246px}
.dark-btn{position:absolute;left:519px;top:396px;width:150px;line-height:38px;border-radius:20px;background:#262b3a;color:#fff;text-align:center;font-family:'Montserrat',sans-serif;font-size:11px;font-weight:600}

/* cost band */
.cost{height:222px;background:var(--dark);text-align:center;color:var(--white);padding-top:50px}
.cost h2{font-family:'Montserrat',sans-serif;font-weight:400;font-size:26px}
.cost h2 b{font-weight:700}
.cost p{font-size:13px;margin-top:8px}
.cost .btn{margin-top:24px;width:186px;line-height:42px;border:2px solid #b24a0c}

/* projects */
.projects{height:575px;position:relative;padding-top:84px}
.project-row{position:absolute;top:230px;left:190px;display:flex;gap:38px}
.project{width:246px;height:266px;background:var(--card);text-align:center}
.project .pic{height:142px}
.project h3{font-family:'Montserrat',sans-serif;font-size:15px;font-weight:600;color:var(--orange);margin-top:22px}
.project p{font-size:11.5px;line-height:17px;margin-top:6px;color:#666}
.project .btn{width:122px;line-height:34px;font-size:11px;margin-top:14px;border:2px solid #b24a0c}
.projects .ring.l{left:94px;top:356px}
.projects .ring.r{right:112px;top:356px}

/* newsletter */
.news{height:70px;background:var(--orange);display:flex;align-items:center;justify-content:center;gap:18px;color:var(--white);font-family:'Montserrat',sans-serif;font-size:21px}
.news b{font-weight:700}
.news .field{width:282px;height:38px;background:#fff;border-radius:20px;display:flex;align-items:center;justify-content:space-between;padding:0 4px 0 18px;font-family:'Open Sans',sans-serif;font-size:11px;color:#777}
.news .go{width:30px;height:30px;border-radius:50%;background:var(--orange);display:flex;align-items:center;justify-content:center}

/* footer */
.footer{height:250px;background:var(--footer);display:flex;padding:58px 0 0 155px;color:#aaa;font-size:11.5px;line-height:18px}
.footer h4{font-family:'Montserrat',sans-serif;color:var(--white);font-size:19px;font-weight:500;margin-bottom:14px;text-transform:uppercase}
.col-a,.col-b{width:248px}
.col-c{width:272px}
.sitemap-row{display:flex;margin-bottom:8px}
.sitemap-row span{width:62px}
.sitemap-row span.w{width:96px}
.sitemap-row span.m{width:76px}
.sitemap .active{color:var(--orange-light)}
.date{color:var(--orange-light);font-size:10.5px}
.ficons{display:flex;gap:8px}
.ficons span{width:28px;height:28px;border-radius:50%;background:#888;display:block}
.fbrand{margin-top:22px;display:flex;align-items:center;gap:8px}
.fbrand i{width:22px;height:22px;border-radius:50%;background:var(--orange);display:block}
.fbrand b{font-family:'Montserrat',sans-serif;font-size:12px;color:var(--orange-light);line-height:1.1}
.copy-bar{height:70px;background:var(--footer-deep);border-top:1px solid #3a3837;text-align:center;color:#999;font-size:11px;line-height:70px}
</style>
</head>
<body>

<header class="top">
  <div class="social" aria-label="Social links"><span></span><span></span><span></span></div>
  <div class="brand"><i></i><b>MESA VERDA<br>LIGHTING</b></div>
  <div class="phone">
    <svg viewBox="0 0 24 24"><path fill="#e8620f" d="M6.6 10.8a15 15 0 0 0 6.6 6.6l2.2-2.2c.3-.3.7-.4 1-.2 1.1.4 2.3.6 3.6.6.6 0 1 .4 1 1V20c0 .6-.4 1-1 1A17 17 0 0 1 3 4c0-.6.4-1 1-1h3.5c.6 0 1 .4 1 1 0 1.3.2 2.5.6 3.6.1.3 0 .7-.2 1z"/></svg>
    555-014-0370
  </div>
</header>

<nav class="nav">
  <a class="active">Home</a><a>About</a><a>Line Card</a><a>Services</a><a>Territory Map</a><a>Photo Gallery</a><a>Blog</a><a>Contact</a>
</nav>

<section class="hero" role="img" aria-label="Industrial plant with lit towers and chimneys at dusk">
  <h1>LEADER IN THE<br>LIGHTENING YOUR WORLD</h1>
  <p>LED experts you can trust</p>
  <a class="btn">Get Connected</a>
  <span class="arrow l"><svg width="10" height="12" viewBox="0 0 10 12"><path d="M7 1 2 6l5 5" stroke="#fff" stroke-width="2" fill="none"/></svg></span>
  <span class="arrow r"><svg width="10" height="12" viewBox="0 0 10 12"><path d="m3 1 5 5-5 5" stroke="#fff" stroke-width="2" fill="none"/></svg></span>
  <span class="dots"></span>
</section>

<section class="services">
  <div class="service">
    <svg class="drop" viewBox="0 0 84 100"><path d="M30 0H54V30A34 34 0 1 1 30 30Z" fill="#e8620f"/><circle cx="42" cy="62" r="26" fill="none" stroke="#fff" stroke-width="2"/><path d="m33 53 18 18M51 53 33 71" stroke="#fff" stroke-width="3"/></svg>
    <h3>Design Assistance</h3>
    <p>We offers interior and exterior lighting design assistance, plus budget estimates to Architects, Engineers, Operations and Facility Management teams.</p>
  </div>
  <div class="service">
    <svg class="drop" viewBox="0 0 84 100"><path d="M30 0H54V30A34 34 0 1 1 30 30Z" fill="#e8620f"/><circle cx="42" cy="62" r="26" fill="none" stroke="#fff" stroke-width="2"/><circle cx="42" cy="61" r="10" fill="#fff"/></svg>
    <h3>Training</h3>
    <p>We offers training to all stakeholders plus coordinated Accredited Continuing Education courses in Lighting.</p>
  </div>
  <div class="service">
    <svg class="drop" viewBox="0 0 84 100"><path d="M30 0H54V30A34 34 0 1 1 30 30Z" fill="#e8620f"/><circle cx="42" cy="62" r="26" fill="none" stroke="#fff" stroke-width="2"/><path d="M31 73V58h7v-7h12v22z" fill="#fff"/></svg>
    <h3>Project Management</h3>
    <p>We offers complete project management of lighting project to include lighting take-off, quotations, RFI guidance, product submittal packages, fixture sample submissions, order tracking and installation review to insure that the lighting project is completed to satisfaction.</p>
  </div>
  <div class="service">
    <svg class="drop" viewBox="0 0 84 100"><path d="M30 0H54V30A34 34 0 1 1 30 30Z" fill="#e8620f"/><circle cx="42" cy="62" r="26" fill="none" stroke="#fff" stroke-width="2"/><path d="M37 49h10v15l-5 9-5-9z" fill="#fff"/></svg>
    <h3>Energy Saving Projects</h3>
    <p>We offers a complete set of solutions for Energy saving, Sustainability and Carbon Footprint reduction initiatives ,Energy Audits and Economic Analysis on relight and retrofit projects.</p>
  </div>
</section>

<section class="welcome">
  <div class="photo" role="img" aria-label="Electrician with tool belt in front of a room under construction"></div>
  <div class="copy">
    <h2>WELCOME</h2>
    <p>Mesa Verda Lighting was established in 1996 and is the leading lighting and controls agency in the region servicing West Texas, New Mexico, and Mexico (Country).</p>
    <p>We are a team of experienced and talented individuals who share the same passion: "Exceed customer and manufacturer expectations by providing high-quality technical support and the best in class customer service", experts in LED Lighting systems for architectural, commercial, industrial, institutional, and residential purposes as well as controls projects.</p>
    <a class="outline">KNOW MORE</a>
  </div>
</section>

<section class="makers">
  <h2 class="title">Our Manufacturer</h2>
  <p class="sub">We are associated with renowned LED light manufacturer company to deliver you the besr product.</p>
  <span class="ring l"><svg width="8" height="12" viewBox="0 0 8 12"><path d="M6 1 1 6l5 5" stroke="#999" stroke-width="1.5" fill="none"/></svg></span>
  <div class="maker-row">
    <div class="maker"><div class="name">NORTHGATE</div><div class="url">www.northgatelighting.example</div></div>
    <div class="maker"><div class="name">SOLARA</div><div class="url">http://solaralighting.example</div></div>
    <div class="maker"><div class="name">LUMIRA LIGHT</div><div class="url">http://solaralighting.example</div></div>
    <div class="maker"><div class="name">VOLTARO</div><div class="url">voltaro.example</div></div>
  </div>
  <span class="ring r"><svg width="8" height="12" viewBox="0 0 8 12"><path d="m2 1 5 5-5 5" stroke="#999" stroke-width="1.5" fill="none"/></svg></span>
  <a class="dark-btn">VIEW PRODUCTS</a>
</section>

<section class="cost">
  <h2>DO YOU NEED HELP TO <b>LOWER YOUR LIGHTING COST?</b></h2>
  <p>Buy our wide range of energy efficiency LED Lights.</p>
  <a class="btn">Contact Now</a>
</section>

<section class="projects">
  <h2 class="title">Our Projects</h2>
  <p class="sub">We compleated a vast range of projects that can prove our expertise to make you trust about our proficiency.</p>
  <span class="ring l"><svg width="8" height="12" viewBox="0 0 8 12"><path d="M6 1 1 6l5 5" stroke="#999" stroke-width="1.5" fill="none"/></svg></span>
  <div class="project-row">
    <div class="project">
      <div class="pic" role="img" aria-label="Warmly lit hotel restaurant interior" style="background:linear-gradient(180deg,#5a3a22,#2a1a10 60%,#8a4a22)"></div>
      <h3>Pinecrest Hotel</h3>
      <p>Lorem ipsum dolor sit amet,<br>consectetur adipisicing elit, sed.</p>
      <a class="btn">DETAILS</a>
    </div>
    <div class="project">
      <div class="pic" role="img" aria-label="Convention center hall with illuminated glass roof" style="background:linear-gradient(180deg,#9fc6e6,#4a6a8a 55%,#2d3c50)"></div>
      <h3>Canyon Convention Center</h3>
      <p>Lorem ipsum dolor sit amet,<br>consectetur adipisicing elit, sed.</p>
      <a class="btn">DETAILS</a>
    </div>
    <div class="project">
      <div class="pic" role="img" aria-label="Shopping plaza with lit fountains at night" style="background:linear-gradient(180deg,#4a2a12,#c8702a 55%,#e8a050)"></div>
      <h3>Liberty Plaza</h3>
      <p>Lorem ipsum dolor sit amet,<br>consectetur adipisicing elit, sed.</p>
      <a class="btn">DETAILS</a>
    </div>
  </div>
  <span class="ring r"><svg width="8" height="12" viewBox="0 0 8 12"><path d="m2 1 5 5-5 5" stroke="#999" stroke-width="1.5" fill="none"/></svg></span>
</section>

<section class="news">
  <span>Subscribe to our <b>Newsletter</b></span>
  <div class="field">Your Email... <span class="go"><svg width="12" height="12" viewBox="0 0 12 12"><path d="M1 6 11 1 8 11 6 7z" fill="#fff"/></svg></span></div>
</section>

<footer class="footer">
  <div class="col-a">
    <h4>Address</h4>
    <p>Mesa Verda Lighting &amp; Design<br>1420 Quarry Ln , Sample City<br>United States 00000</p>
    <p style="margin-top:14px;display:flex;align-items:center;gap:8px"><svg width="12" height="12" viewBox="0 0 24 24"><path fill="#e8620f" d="M6.6 10.8a15 15 0 0 0 6.6 6.6l2.2-2.2c.3-.3.7-.4 1-.2 1.1.4 2.3.6 3.6.6.6 0 1 .4 1 1V20c0 .6-.4 1-1 1A17 17 0 0 1 3 4c0-.6.4-1 1-1h3.5c.6 0 1 .4 1 1 0 1.3.2 2.5.6 3.6.1.3 0 .7-.2 1z"/></svg>555-014-0370</p>
  </div>
  <div class="col-b">
    <h4>Sitemap</h4>
    <div class="sitemap">
      <div class="sitemap-row"><span class="active">Home</span><span>About</span><span>Line Card</span></div>
      <div class="sitemap-row"><span>Services</span><span class="w">Territory Map</span></div>
      <div class="sitemap-row"><span class="w">Photo Gallery</span><span>Blog</span></div>
      <div class="sitemap-row"><span class="m">Contact</span><span>Terms</span></div>
    </div>
  </div>
  <div class="col-c">
    <h4>Our Blog</h4>
    <p>Lorem ipsum dolor sit amet,<br>consectetur adipisicing elit, sed do<br>eiusmod tempor incididunt ut et.</p>
    <p class="date">May 28, 2017</p>
    <p style="margin-top:12px">Read More &gt;</p>
  </div>
  <div>
    <h4>Follow Us</h4>
    <div class="ficons"><span></span><span></span><span></span></div>
    <div class="fbrand"><i></i><b>MESA VERDA<br>LIGHTING</b></div>
  </div>
</footer>
<div class="copy-bar">© 2016 Mesa Verda Lighting &amp; Design. All Rights Reserved.</div>

</body>
</html>
```